Business Card For Kelmora Financial Consulting

Hi, I would like a business card designed. Bold, modern.
Please use the same design as the logo. I have also attached the website design to see the overall theme.
Wordmark Font
Color: Hex: #01AEF7

```html
<!DOCTYPE html>
<html lang="en">
<head>
<meta charset="utf-8">
<title>Kelmora Financial Consulting – Business Card</title>
<link rel="stylesheet" href="https://fonts.googleapis.com/css2?family=Poppins:wght@400;500;600;700&display=swap">
<style>
  :root {
    --brand-blue: #0398d6;
    --brand-navy: #13202b;
    --card-white: #f7f7f7;
    --ink: #111111;
    --backdrop: #e4e6e8;
  }
  * { box-sizing: border-box; margin: 0; padding: 0; }
  html, body { width: 1200px; height: 900px; overflow: hidden; }
  body {
    background: var(--backdrop);
    font-family: "Poppins", sans-serif;
    position: relative;
  }
  .card {
    position: absolute;
    left: 250px;
    width: 700px;
    height: 400px;
    background: var(--card-white);
    overflow: hidden;
    box-shadow: 0 6px 18px rgba(0,0,0,0.15);
  }
  .card--back { top: 30px; }
  .card--front { top: 470px; }
  .card-shapes { position: absolute; inset: 0; }
  .band-navy { fill: var(--brand-navy); }
  .band-blue { fill: var(--brand-blue); }

  /* back */
  .back-wordmark {
    position: absolute; top: 95px; left: 0; width: 100%;
    text-align: center; color: var(--brand-blue);
    font-weight: 700; font-size: 52px; letter-spacing: 4px;
  }
  .back-url {
    position: absolute; left: 20px; top: 307px; width: 380px;
    text-align: center;
    color: #fff; font-weight: 600; font-size: 15px; letter-spacing: 1.5px;
  }
  .back-brand { position: absolute; left: 515px; top: 248px; }

  /* shared brand lockup */
  .brand { display: flex; align-items: center; gap: 10px; }
  .brand-square { width: 30px; height: 30px; background: var(--brand-blue); }
  .brand-text { display: flex; flex-direction: column; line-height: 1; }
  .brand-name { color: #fff; font-weight: 700; font-size: 28px; letter-spacing: 2px; }
  .brand-sub { color: #fff; font-weight: 700; font-size: 9px; letter-spacing: 9px; margin-top: 6px; }

  /* front */
  .front-corner-square {
    position: absolute; right: 32px; top: 28px;
    width: 60px; height: 60px; background: var(--brand-blue);
  }
  .person { position: absolute; top: 75px; left: 0; width: 100%; text-align: center; }
  .person-name { color: var(--brand-blue); font-weight: 700; font-size: 26px; letter-spacing: 0.5px; }
  .person-title { color: var(--ink); font-weight: 600; font-size: 17px; margin-top: -4px; }
  .address {
    position: absolute; top: 170px; left: 0; width: 100%;
    text-align: center; color: var(--ink); font-weight: 600; font-size: 14px; line-height: 1.6;
  }
  .contacts {
    position: absolute; top: 236px; left: 160px;
    display: flex; gap: 22px; font-size: 13px; color: var(--ink); font-weight: 500;
  }
  .contact-label { color: var(--brand-blue); font-weight: 400; }
  .front-brand { position: absolute; left: 40px; top: 318px; }
  .front-url {
    position: absolute; left: 440px; top: 323px; width: 250px;
    text-align: center; white-space: nowrap;
    color: #fff; font-weight: 600; font-size: 13px; letter-spacing: 1px;
  }
</style>
</head>
<body>

  <section class="card card--back" aria-label="Card back">
    <svg class="card-shapes" viewBox="0 0 700 400" aria-hidden="true">
      <polygon class="band-navy" points="490,225 700,225 700,320 455,320"/>
      <polygon class="band-blue" points="0,290 440,290 415,350 0,350"/>
    </svg>
    <div class="back-wordmark">KELMORA</div>
    <div class="back-brand brand">
      <div class="brand-text">
        <span class="brand-name">KELMORA</span>
        <span class="brand-sub">CONSULTING</span>
      </div>
    </div>
    <div class="back-url">www.kelmoraconsulting.com</div>
  </section>

  <section class="card card--front" aria-label="Card front">
    <svg class="card-shapes" viewBox="0 0 700 400" aria-hidden="true">
      <polygon class="band-navy" points="0,270 390,270 440,400 0,400"/>
      <polygon class="band-blue" points="420,290 700,290 700,375 450,375"/>
    </svg>
    <div class="front-corner-square"></div>
    <div class="person">
      <div class="person-name">DANA M. HOLLIS</div>
      <div class="person-title">President</div>
    </div>
    <div class="address">
      2250 Birchwood Park Road NE Ste 310,<br>
      Lanford, OH 43990
    </div>
    <div class="contacts">
      <span><span class="contact-label">Phone:</span> 555-214-7730</span>
      <span><span class="contact-label">Fax:</span> 555-880-4412</span>
      <span><span class="contact-label">Email:</span> hello@kelmoraco.com</span>
    </div>
    <div class="front-brand brand">
      <div class="brand-square"></div>
      <div class="brand-text">
        <span class="brand-name">KELMORA</span>
        <span class="brand-sub">CONSULTING</span>
      </div>
    </div>
    <div class="front-url">www.kelmoraconsulting.com</div>
  </section>

</body>
</html>
```